Veterinary Hospital Business Card

We have recently updated our logo and wish to have a business card designed incorporating the new look and flow. We are a full service veterinary hospital also offering laser therapy, boarding, and grooming. Our website is www.marlowpaws.com

Industry/Entity Type

Veterinary

```html
<!DOCTYPE html>
<html lang="en">
<head>
<meta charset="utf-8">
<title>Marlow Animal Hospital – Business Card</title>
<link rel="stylesheet" href="https://fonts.googleapis.com/css2?family=Saira:wght@400;500;700&family=Saira+Condensed:wght@700&display=swap">
<style>
  :root {
    --stage: #d8dbde;
    --card: #f1f2f4;
    --card-edge: #e4e6e9;
    --blue: #4b7fa1;
    --blue-light: #8fb3cc;
    --navy: #1f4a6b;
    --ink: #3f5d74;
    --band-text: #eaf2f8;
    --map: #dcdfe3;
  }
  * { box-sizing: border-box; margin: 0; padding: 0; }
  html, body { width: 1200px; height: 899px; overflow: hidden; }
  body { background: var(--stage); position: relative; font-family: "Saira", sans-serif; }

  .card {
    position: absolute; left: 250px; width: 700px; height: 400px;
    background: var(--card); overflow: hidden;
    box-shadow: 0 6px 18px rgba(0,0,0,.18);
  }
  .card--front { top: 30px; }
  .card--back { top: 469px; }
  .card__shapes { position: absolute; inset: 0; }

  .map-area {
    position: absolute; border-radius: 40% 50% 45% 40%;
    background: radial-gradient(ellipse at center, var(--map) 0%, rgba(220,223,227,0) 72%);
  }

  .brand {
    position: absolute; color: var(--navy);
    font-family: "Saira Condensed", sans-serif; font-weight: 700;
    text-transform: uppercase; line-height: .92; letter-spacing: .5px;
  }
  .brand__mark {
    display: block; width: 34px; height: 34px; border-radius: 50%;
    background: var(--blue); margin-bottom: 10px;
  }
  .card--front .brand { left: 200px; top: 92px; font-size: 52px; }
  .card--back .brand { left: 110px; top: 62px; font-size: 44px; }

  .front__web {
    position: absolute; left: 420px; top: 222px;
    font-size: 15px; color: var(--ink); letter-spacing: .5px;
  }

  .person { position: absolute; left: 372px; top: 98px; color: var(--blue); }
  .person__name { font-size: 30px; font-weight: 400; letter-spacing: 2px; text-transform: uppercase; line-height: 1; }
  .person__role { font-size: 12px; font-weight: 500; letter-spacing: 1.6px; text-transform: uppercase; color: var(--ink); margin-top: 4px; }

  .contact-band {
    position: absolute; left: 0; right: 0; bottom: 0; height: 96px;
    background: var(--blue); display: flex; align-items: center; padding: 0 22px;
    color: var(--band-text); font-size: 13px; letter-spacing: .6px;
  }
  .contact-band__col { display: flex; flex-direction: column; gap: 12px; padding: 0 20px; }
  .contact-band__col + .contact-band__col { border-left: 1px solid rgba(255,255,255,.55); }
  .contact-item { display: flex; align-items: center; gap: 8px; white-space: nowrap; }
  .contact-item svg { width: 14px; height: 14px; flex: none; }
  .contact-item--address { align-items: flex-start; line-height: 1.35; }
</style>
</head>
<body>

  <section class="card card--front" aria-label="Card front">
    <div class="map-area" role="img" aria-label="Faint world map backdrop" style="left:120px; top:40px; width:520px; height:300px;"></div>
    <svg class="card__shapes" viewBox="0 0 700 400" aria-hidden="true">
      <polygon points="0,90 175,400 0,400" fill="var(--blue)"/>
      <rect x="70" y="255" width="62" height="62" fill="var(--blue-light)" opacity=".85"/>
      <polygon points="515,0 700,0 700,300" fill="var(--blue)"/>
      <rect x="590" y="110" width="58" height="58" fill="var(--blue-light)" opacity=".85"/>
    </svg>
    <div class="brand">
      <span class="brand__mark"></span>
      Marlow<br>Animal<br>Hospital
    </div>
    <p class="front__web">www.marlowpaws.com</p>
  </section>

  <section class="card card--back" aria-label="Card back">
    <div class="map-area" role="img" aria-label="Faint world map backdrop" style="left:80px; top:10px; width:560px; height:280px;"></div>
    <svg class="card__shapes" viewBox="0 0 700 400" aria-hidden="true">
      <polygon points="520,0 700,0 700,190" fill="var(--blue)"/>
      <rect x="612" y="38" width="52" height="52" fill="var(--blue-light)" opacity=".85"/>
    </svg>
    <div class="brand">
      <span class="brand__mark"></span>
      Marlow<br>Animal<br>Hospital
    </div>
    <div class="person">
      <p class="person__name">Ellis Varga</p>
      <p class="person__role">General Manager</p>
    </div>

    <div class="contact-band">
      <div class="contact-band__col">
        <span class="contact-item">
          <svg viewBox="0 0 16 16"><path d="M4 1.5l2.2 3-1.3 1.6c.9 1.9 2.3 3.3 4.3 4.3l1.6-1.3 3 2.2-1.2 2.6C7.5 13.6 2.4 8.5 1.4 2.7z" fill="currentColor"/></svg>
          012 555 0148
        </span>
        <span class="contact-item">
          <svg viewBox="0 0 16 16"><rect x="4" y="1" width="8" height="14" rx="1.5" fill="none" stroke="currentColor" stroke-width="1.5"/><circle cx="8" cy="12.3" r=".9" fill="currentColor"/></svg>
          012 555 0148
        </span>
      </div>
      <div class="contact-band__col">
        <span class="contact-item">
          <svg viewBox="0 0 16 16"><rect x="1" y="3" width="14" height="10" rx="1" fill="currentColor"/><path d="M1.5 3.8L8 9l6.5-5.2" fill="none" stroke="var(--blue)" stroke-width="1.3"/></svg>
          hello@marlowpaws.com
        </span>
        <span class="contact-item">
          <svg viewBox="0 0 16 16"><circle cx="8" cy="8" r="6.5" fill="none" stroke="currentColor" stroke-width="1.4"/><ellipse cx="8" cy="8" rx="2.8" ry="6.5" fill="none" stroke="currentColor" stroke-width="1.2"/><path d="M1.5 8h13" stroke="currentColor" stroke-width="1.2"/></svg>
          www.marlowpaws.com
        </span>
      </div>
      <div class="contact-band__col">
        <span class="contact-item contact-item--address">
          <svg viewBox="0 0 16 16"><path d="M8 1a4.8 4.8 0 0 0-4.8 4.8C3.2 9.6 8 15 8 15s4.8-5.4 4.8-9.2A4.8 4.8 0 0 0 8 1z" fill="currentColor"/><circle cx="8" cy="5.8" r="1.8" fill="var(--blue)"/></svg>
          27 Harbor Lane, 2nd floor<br>West Wing
        </span>
      </div>
    </div>
  </section>

</body>
</html>
```